New Web Design Project

New Roofing Website homepage mockup

Complete design document here: https://files.plorvex.net/doc/7tQmZrA2kLwP9xVbN4cYhE3sJdF8gUoR6iKe1nTy/edit?usp=sharing
Updates

Number of Pages Required

1 page

Font styles to use
Sans Serif

```html
<!DOCTYPE html>
<html lang="en">
<head>
<meta charset="utf-8">
<title>Evergate Roofing</title>
<link href="https://fonts.googleapis.com/css2?family=Bebas+Neue&family=Poppins:wght@400;500;600&display=swap" rel="stylesheet">
<style>
:root{
  --blue:#28a2dc;
  --slate:#5c5e62;
  --ink:#55575b;
  --text:#5f6165;
  --rule:#e3e3e3;
  --white:#ffffff;
}
html,body{margin:0;padding:0;overflow:hidden;background:var(--white);}
.page{position:relative;width:1200px;height:4769px;overflow:hidden;font-family:'Poppins',sans-serif;color:var(--text);}
.page *{box-sizing:border-box;}
.abs{position:absolute;}
.backdrop{position:absolute;left:0;top:0;}
.heading{font-family:'Bebas Neue',sans-serif;color:var(--ink);font-weight:400;margin:0;letter-spacing:1px;line-height:1;}
.section-title{position:absolute;left:0;width:1200px;text-align:center;font-size:54px;}

/* header */
.brand{position:absolute;left:87px;top:38px;display:flex;align-items:center;gap:8px;font-weight:600;font-size:17px;color:var(--blue);letter-spacing:.5px;}
.brand-square{width:14px;height:14px;background:var(--blue);}
.nav{position:absolute;top:44px;left:0;width:1200px;height:20px;font-size:12.5px;color:#4b4d51;}
.nav span{position:absolute;top:0;white-space:nowrap;}
.nav .home{left:366px;top:-2px;}

/* hero */
.hero-title{position:absolute;top:250px;left:0;width:1200px;text-align:center;font-size:78px;color:var(--white);}
.btn-light{position:absolute;background:var(--white);color:#3c3e42;font-size:12px;font-weight:600;letter-spacing:.6px;display:flex;align-items:center;justify-content:center;}

/* services */
.service-photo{position:absolute;top:944px;width:406px;height:245px;}
.service-card{position:absolute;top:1152px;width:370px;height:181px;background:var(--white);box-shadow:0 4px 14px rgba(0,0,0,.13);border-bottom:3px solid #cfe9f6;padding:22px 24px 0;}
.service-card h3{font-size:25px;margin:0 0 8px;}
.service-card p{margin:0;font-size:13px;line-height:17px;color:var(--text);}
.btn-blue{position:absolute;left:24px;top:113px;width:120px;height:39px;background:var(--blue);color:var(--white);font-size:11.5px;font-weight:600;display:flex;align-items:center;justify-content:center;letter-spacing:.5px;}

/* about */
.about-art{position:absolute;left:89px;top:1596px;width:563px;height:265px;background:linear-gradient(135deg,#3a3b3e 0%,#6c6b68 50%,#a89a89 100%);}
.about-title{position:absolute;left:711px;top:1628px;font-size:50px;color:var(--white);}
.about-copy{position:absolute;left:711px;top:1684px;width:405px;margin:0;font-size:14px;line-height:20.5px;color:#eef0f2;}

/* roof types */
.roof-tile{position:absolute;top:2193px;width:200px;height:229px;}
.roof-tile .label{position:absolute;left:0;bottom:12px;width:100%;text-align:center;font-family:'Bebas Neue',sans-serif;font-size:24px;color:var(--white);letter-spacing:.5px;}
.roof-tile .arrow{position:absolute;right:14px;bottom:20px;}
.divider{position:absolute;left:87px;top:2513px;width:1024px;height:1px;background:var(--rule);}

/* projects */
.project{position:absolute;width:274px;height:211px;}
.project-label{position:absolute;inset:12px;border:4px solid rgba(255,255,255,.75);display:flex;align-items:center;justify-content:center;font-family:'Bebas Neue',sans-serif;font-size:34px;color:var(--white);background:rgba(255,255,255,.25);}

/* cta */
.cta-title{position:absolute;left:0;top:3235px;width:1200px;text-align:center;font-size:56px;color:var(--white);}
.cta-copy{position:absolute;left:260px;top:3292px;width:680px;margin:0;text-align:center;font-size:16px;line-height:19px;color:var(--white);}

/* testimonial */
.quote{position:absolute;left:296px;top:3858px;width:610px;margin:0;text-align:center;font-size:13.5px;line-height:22px;color:var(--text);}
.client-name{position:absolute;left:0;top:4030px;width:1200px;text-align:center;font-size:28px;}
.client-town{position:absolute;left:0;top:4058px;width:1200px;text-align:center;font-size:17px;color:#8a8c90;}
.round-arrow{position:absolute;width:46px;height:46px;border-radius:50%;background:#e8e8e8;}

/* footer */
.footer-brand{position:absolute;left:0;top:4320px;width:1200px;display:flex;justify-content:center;align-items:center;gap:10px;font-weight:600;font-size:26px;color:var(--blue);letter-spacing:.5px;}
.footer-brand .brand-square{width:22px;height:22px;}
.footer-col{position:absolute;top:4422px;}
.footer-col h4{font-family:'Bebas Neue',sans-serif;font-weight:400;font-size:22px;color:var(--white);margin:0 0 22px;letter-spacing:.5px;}
.footer-col ul{list-style:none;margin:0;padding:0;font-size:13px;line-height:27px;color:#eef0f2;}
.contact-item{position:relative;padding-left:24px;font-size:13px;line-height:18px;color:#eef0f2;margin-bottom:19px;}
.contact-item b{font-weight:600;display:block;}
.contact-item svg{position:absolute;left:0;top:2px;}
.newsletter{position:absolute;left:750px;top:4474px;width:361px;height:32px;border-bottom:1px solid rgba(255,255,255,.55);font-size:12.5px;color:#eef0f2;padding-left:24px;padding-top:5px;}
.legal{position:absolute;top:4703px;font-size:12px;color:#eef0f2;white-space:nowrap;}
.social{position:absolute;top:4674px;width:34px;height:34px;border-radius:50%;background:#6c6e72;}
.to-top{position:absolute;left:1128px;top:4669px;width:44px;height:44px;border-radius:50%;background:var(--blue);display:flex;align-items:center;justify-content:center;}
</style>
</head>
<body>
<div class="page">

  <!-- background bands and connectors -->
  <svg class="backdrop" width="1200" height="4769" viewBox="0 0 1200 4769" aria-hidden="true">
    <polygon points="0,1537 407,1439 1200,1555 1200,1898 407,2019 0,1907" fill="#5c5e62"/>
    <polygon points="0,3163 1200,3163 1200,3445 407,3608 0,3506" fill="#28a2dc"/>
    <polygon points="0,4293 407,4189 1200,4293 1200,4769 0,4769" fill="#5c5e62"/>
    <g stroke="#28a2dc" stroke-width="2">
      <line x1="407" y1="778" x2="407" y2="850"/>
      <line x1="407" y1="2019" x2="407" y2="2100"/>
      <line x1="407" y1="3608" x2="407" y2="3689"/>
      <line x1="407" y1="4108" x2="407" y2="4189"/>
    </g>
    <line x1="407" y1="1439" x2="407" y2="1517" stroke="#ffffff" stroke-width="2"/>
    <g fill="#28a2dc">
      <circle cx="407" cy="852" r="5"/>
      <circle cx="407" cy="2102" r="5"/>
      <circle cx="407" cy="3691" r="5"/>
      <circle cx="407" cy="4108" r="5"/>
    </g>
    <circle cx="407" cy="1519" r="5" fill="#ffffff"/>
  </svg>

  <!-- header -->
  <div class="brand"><span class="brand-square"></span>EVERGATE ROOFING</div>
  <nav class="nav">
    <svg class="home abs" width="22" height="20" viewBox="0 0 22 20" aria-hidden="true"><path d="M11 1 L21 10 H18 V19 H13 V13 H9 V19 H4 V10 H1 Z" fill="#28a2dc"/></svg>
    <span style="left:411px">SERVICES</span>
    <span style="left:508px">ABOUT</span>
    <span style="left:589px">TYPES OF ROOFS</span>
    <span style="left:733px">RECENT PROJECTS</span>
    <span style="left:890px">INSTANT ESTIMATE</span>
    <span style="left:1047px">CONTACT</span>
  </nav>

  <!-- hero -->
  <svg class="abs" style="left:0;top:104px" width="1200" height="674" viewBox="0 104 1200 674" role="img" aria-label="Photo of a large grey shingled colonial house with a green lawn under a blue sky">
    <defs>
      <linearGradient id="heroSky" x1="0" y1="0" x2="0" y2="1">
        <stop offset="0" stop-color="#6f9fd4"/>
        <stop offset=".38" stop-color="#b9cfe3"/>
        <stop offset=".55" stop-color="#8e9495"/>
        <stop offset=".78" stop-color="#9a9d98"/>
        <stop offset="1" stop-color="#4f7a34"/>
      </linearGradient>
    </defs>
    <polygon points="0,104 1200,104 1200,583 472,778 0,620" fill="url(#heroSky)"/>
  </svg>
  <h1 class="heading hero-title">Built Right Built To Last</h1>
  <div class="btn-light" style="left:485px;top:337px;width:228px;height:44px;">GET AN INSTANT&nbsp; ESTIMATE</div>

  <!-- services -->
  <h2 class="heading section-title" style="top:878px">Our Services</h2>
  <div class="service-photo" style="left:174px;background:linear-gradient(120deg,#5b6065 0%,#7c8185 45%,#b8d531 60%,#3e4a5c 100%)" role="img" aria-label="Photo of a roofer in a hard hat installing slate tiles"></div>
  <div class="service-photo" style="left:600px;background:linear-gradient(160deg,#b4622c 0%,#d48a4e 35%,#9ea3a8 60%,#3d3f43 100%)" role="img" aria-label="Photo of hands hammering shingles during a roof repair"></div>
  <div class="service-card" style="left:193px">
    <h3 class="heading">Roof Installation</h3>
    <p>Lorem ipsum dolor sit ametadipisicing elit sed do eiusmod tempor incididunt&nbsp; dolore...</p>
    <div class="btn-blue">VIEW DETAILS</div>
  </div>
  <div class="service-card" style="left:619px">
    <h3 class="heading">Roof Repair</h3>
    <p>Lorem ipsum dolor sit ametadipisicing elit sed do eiusmod tempor incididunt&nbsp; dolore...</p>
    <div class="btn-blue">VIEW DETAILS</div>
  </div>

  <!-- about -->
  <div class="about-art" role="img" aria-label="Illustration of cedar shingle rooftops with windows"></div>
  <h2 class="heading about-title">About Us</h2>
  <p class="about-copy">After over a decade of general contracting, we continue to see a repetitive trend by the roof purchase process where homeowners are constantly left confused, nervous, and worried when they need a new roof. As one of the most important features of keeping your home safe, this is unacceptable. Evergate Roofing was created to break this trend.</p>

  <!-- roof types -->
  <h2 class="heading section-title" style="top:2134px">Types Of Roofs</h2>
  <div class="roof-tile" style="left:87px;background:linear-gradient(170deg,#d9905a,#a4552a 70%,#6b331a)" role="img" aria-label="Close-up of cedar shake roofing">
    <span class="label">Cedar</span>
    <svg class="arrow" width="18" height="10" viewBox="0 0 18 10" aria-hidden="true"><path d="M0 5H16M12 1L16 5L12 9" stroke="#fff" stroke-width="1.2" fill="none" opacity=".7"/></svg>
  </div>
  <div class="roof-tile" style="left:293px;background:linear-gradient(160deg,#4c4d50,#1e1f21 75%,#0f0f10)" role="img" aria-label="Close-up of dark metal shingle roofing">
    <span class="label">Metal</span>
    <svg class="arrow" width="18" height="10" viewBox="0 0 18 10" aria-hidden="true"><path d="M0 5H16M12 1L16 5L12 9" stroke="#fff" stroke-width="1.2" fill="none" opacity=".7"/></svg>
  </div>
  <div class="roof-tile" style="left:499px;background:linear-gradient(170deg,#7a7d80,#4a4c50 60%,#2c2d30)" role="img" aria-label="Close-up of grey slate roofing">
    <span class="label">Slate</span>
    <svg class="arrow" width="18" height="10" viewBox="0 0 18 10" aria-hidden="true"><path d="M0 5H16M12 1L16 5L12 9" stroke="#fff" stroke-width="1.2" fill="none" opacity=".7"/></svg>
  </div>
  <div class="roof-tile" style="left:705px;background:linear-gradient(160deg,#5d5e61,#3d3e41 60%,#252628)" role="img" aria-label="Close-up of asphalt shingle roofing">
    <span class="label">Asphalt</span>
    <svg class="arrow" width="18" height="10" viewBox="0 0 18 10" aria-hidden="true"><path d="M0 5H16M12 1L16 5L12 9" stroke="#fff" stroke-width="1.2" fill="none" opacity=".7"/></svg>
  </div>
  <div class="roof-tile" style="left:911px;background:linear-gradient(180deg,#8a4a3a 0%,#5b3a33 22%,#3a3b3d 40%,#232426 100%)" role="img" aria-label="Flat rubber membrane roof beside a brick wall">
    <span class="label">Rubber</span>
    <svg class="arrow" width="18" height="10" viewBox="0 0 18 10" aria-hidden="true"><path d="M0 5H16M12 1L16 5L12 9" stroke="#fff" stroke-width="1.2" fill="none" opacity=".7"/></svg>
  </div>
  <div class="divider"></div>

  <!-- recent projects -->
  <h2 class="heading section-title" style="top:2580px">Recent Projects</h2>
  <div class="project" style="left:181px;top:2643px;background:linear-gradient(180deg,#7aa3d6 0%,#c6d3df 40%,#8e9294 70%,#8a8a86 100%)" role="img" aria-label="Grey colonial house with new roof and driveway"></div>
  <div class="project" style="left:463px;top:2643px;background:linear-gradient(180deg,#8a9db8 0%,#c9d1d8 45%,#e9ecee 60%,#55575b 100%)" role="img" aria-label="White cupola with weathervane on a shingled roof"></div>
  <div class="project" style="left:745px;top:2643px;background:linear-gradient(180deg,#97b5d4 0%,#cfd7dc 40%,#8f928f 70%,#5f8a3c 100%)" role="img" aria-label="Large grey house with landscaped lawn"></div>
  <div class="project" style="left:181px;top:2863px;background:linear-gradient(180deg,#7ea6d8 0%,#b9c7d2 35%,#3c3e44 55%,#d8dadb 100%)" role="img" aria-label="House roof under construction with curved dormer"></div>
  <div class="project" style="left:463px;top:2863px;background:linear-gradient(180deg,#a9adb0,#8d9093)" role="img" aria-label="Grey house with garage in Lexington">
    <div class="project-label">Lexington</div>
  </div>
  <div class="project" style="left:745px;top:2863px;background:linear-gradient(135deg,#6b4f3f 0%,#9a8a7c 40%,#d9d1c6 70%,#b9ada0 100%)" role="img" aria-label="Cedar shingle roof curving over an arched window"></div>

  <!-- call to action -->
  <h2 class="heading cta-title">Choose Your Roof Type</h2>
  <p class="cta-copy">A roof does more than keep the rain off your head. It protects&nbsp; your biggest investment – your home</p>
  <div class="btn-light" style="left:441px;top:3345px;width:318px;height:46px;font-size:11.5px;">CALCULATE THE COST OF A NEW ROOF NOW</div>
  <svg class="abs" style="left:195px;top:3410px" width="865" height="198" viewBox="195 3410 865 198" role="img" aria-label="Photo of a grey clapboard house with a newly shingled roof">
    <defs>
      <linearGradient id="ctaHouse" x1="0" y1="0" x2="0" y2="1">
        <stop offset="0" stop-color="#8e9092"/>
        <stop offset=".45" stop-color="#6f7174"/>
        <stop offset="1" stop-color="#a8aaa8"/>
      </linearGradient>
    </defs>
    <polygon points="195,3410 1060,3410 1060,3474 407,3608 195,3555" fill="url(#ctaHouse)"/>
  </svg>

  <!-- testimonials -->
  <h2 class="heading section-title" style="top:3714px">Happy Clients</h2>
  <svg class="abs" style="left:560px;top:3791px" width="80" height="46" viewBox="0 0 80 46" aria-hidden="true">
    <g fill="#28a2dc">
      <circle cx="18" cy="17" r="16"/><path d="M30 24 Q30 40 12 46 Q24 36 22 26 Z"/>
      <circle cx="60" cy="17" r="16"/><path d="M72 24 Q72 40 54 46 Q66 36 64 26 Z"/>
    </g>
  </svg>
  <p class="quote">"We needed to put a new roof on our house, as well as repair a sagging porch roof. Shingles had been flying off and we had had several leaks. Owen provided a very reasonable estimate – well below some of the other HomeReview companies. The work was done very promptly and professionally. A couple of issues that arose were settled to our satisfaction and Owen took full ownership of the situation. It was very clear that customer satisfaction is a priority for this company. I would definitely recommend and hire again."</p>
  <div class="heading client-name">Derek</div>
  <div class="client-town">Millbrook</div>
  <div class="round-arrow" style="left:90px;top:3905px">
    <svg class="abs" style="left:19px;top:18px" width="8" height="10" viewBox="0 0 8 10" aria-hidden="true"><path d="M6 1L2 5L6 9" stroke="#666" stroke-width="1.4" fill="none"/></svg>
  </div>
  <div class="round-arrow" style="left:1062px;top:3905px">
    <svg class="abs" style="left:19px;top:18px" width="8" height="10" viewBox="0 0 8 10" aria-hidden="true"><path d="M2 1L6 5L2 9" stroke="#666" stroke-width="1.4" fill="none"/></svg>
  </div>

  <!-- footer -->
  <div class="footer-brand"><span class="brand-square"></span>EVERGATE ROOFING</div>

  <div class="footer-col" style="left:87px">
    <h4>Quick Links</h4>
    <ul><li>Services</li><li>About</li><li>Types Of Roofs</li><li>Recent Projects</li><li>Instant Estimate</li><li>Contact Us</li></ul>
  </div>
  <div class="footer-col" style="left:261px">
    <h4>Roofs Types</h4>
    <ul style="padding-left:8px"><li>Roofs Cedar</li><li>Roofs Metal</li><li>Roofs Slate</li><li>Roofs Asphalt</li><li>Roofs Rubber</li></ul>
  </div>
  <div class="footer-col" style="left:432px">
    <h4>Contact</h4>
    <div class="contact-item">
      <svg width="12" height="12" viewBox="0 0 12 12" aria-hidden="true"><path d="M2 1L4.5 1L5.5 4L4 5Q5 7.5 7 8L8 6.5L11 7.5L11 10Q10.5 11 9 11Q1 9.5 1 2Q1 1 2 1Z" fill="#28a2dc"/></svg>
      <b>Phone</b>555-014-2290
    </div>
    <div class="contact-item">
      <svg width="12" height="10" viewBox="0 0 12 10" aria-hidden="true"><rect x="0" y="0" width="12" height="10" rx="1" fill="#28a2dc"/><path d="M0.5 1L6 5.5L11.5 1" stroke="#5c5e62" fill="none"/></svg>
      <b>Email</b>OwenHale@EvergateRoofing.com
    </div>
    <div class="contact-item">
      <svg width="11" height="14" viewBox="0 0 11 14" aria-hidden="true"><path d="M5.5 0A5 5 0 0 1 10.5 5C10.5 9 5.5 14 5.5 14S0.5 9 0.5 5A5 5 0 0 1 5.5 0Z" fill="#28a2dc"/><circle cx="5.5" cy="5" r="2" fill="#5c5e62"/></svg>
      <b>Location</b>48 Alder Lane, Millbrook MA 01999
    </div>
  </div>
  <div class="footer-col" style="left:750px">
    <h4>Keep In The Loop</h4>
  </div>
  <div class="newsletter">
    <svg class="abs" style="left:0;top:9px" width="13" height="10" viewBox="0 0 13 10" aria-hidden="true"><rect width="13" height="10" rx="1" fill="#eef0f2"/><path d="M0.5 1L6.5 5.5L12.5 1" stroke="#5c5e62" fill="none"/></svg>
    Enter your email
    <svg class="abs" style="right:4px;top:6px" width="18" height="16" viewBox="0 0 18 16" aria-hidden="true"><path d="M0 7L18 0L14 16L9 11L15 3L7 10Z" fill="#28a2dc"/></svg>
  </div>

  <span class="legal" style="left:87px">© 2020 Evergate Roofing</span>
  <span class="legal" style="left:265px">Privacy Policy</span>
  <span class="legal" style="left:379px">Terms &amp; Conditions</span>
  <span class="legal" style="left:528px">Informed Constent</span>
  <div class="social" style="left:755px" aria-label="Social profile"></div>
  <div class="social" style="left:798px" aria-label="Social profile"></div>
  <div class="social" style="left:842px" aria-label="Social profile"></div>
  <div class="to-top">
    <svg width="12" height="8" viewBox="0 0 12 8" aria-hidden="true"><path d="M1 7L6 2L11 7" stroke="#fff" stroke-width="1.6" fill="none"/></svg>
  </div>

</div>
</body>
</html>
```